Lunaria Set Social Media Graphics

Focusing on the Lunaria Harmony Set product, create 6-7 individual social media graphics (square size). For the color scheme of the graphics, they should all be complementary with the Lunaria Harmony Set bottle colors.

Note: each graphic should have one of the pictures of the bottles (3 product bundle) on it and/or one of the images with a person on it (several pics attached)/only use stock photography that I provided.

Target Market(s)

women over 50 dealing with menopause

Industry/Entity Type

health and wellness

Requirements
Must have
• the pictures/images I provided

```html
<!DOCTYPE html>
<html lang="en">
<head>
<meta charset="utf-8">
<title>Lunaria Set Social Media Graphics</title>
<link href="https://fonts.googleapis.com/css2?family=Montserrat:wght@300;400;500;600;700;800&display=swap" rel="stylesheet">
<style>
:root{
  --board:#000000;
  --rose:#d35a68;
  --rose-deep:#cf5562;
  --rose-soft:#e7b6bd;
  --rose-pale:#f1d3d7;
  --ink:#111111;
  --white:#ffffff;
  --teal:#14a28d;
  --forest:#2f6f5b;
  --tag:#e4e4e6;
}
*{margin:0;padding:0;box-sizing:border-box}
html,body{width:1197px;height:1200px;overflow:hidden;background:var(--board)}
body{position:relative;font-family:'Montserrat',sans-serif}
.post{position:absolute;width:532px;height:532px;overflow:hidden}
.post svg{position:absolute;inset:0;width:532px;height:532px}
.post--weight{left:37px;top:38px}
.post--struggle{left:613px;top:38px}
.post--relief{left:37px;top:609px;background:var(--white)}
.post--tracks{left:613px;top:609px;background:var(--white)}
.txt{position:absolute;white-space:nowrap;line-height:1}
.tag-label{font-weight:600;color:var(--rose)}
.badge{fill:var(--rose)}
.badge-ring{fill:none;stroke:var(--white);stroke-width:1.2;stroke-dasharray:3 2}
.icon-line{fill:none;stroke:var(--white);stroke-width:1.6;stroke-linecap:round;stroke-linejoin:round}
.bundle-name{font-family:'Montserrat',sans-serif;font-weight:600;fill:var(--rose)}
</style>
</head>
<body>

<!-- Post 1: weight loss -->
<section class="post post--weight">
  <svg viewBox="0 0 532 532">
    <defs>
      <symbol id="ico-meno" viewBox="-10 -10 20 20">
        <circle class="icon-line" cx="0" cy="-3" r="5"/>
        <path class="icon-line" d="M0 2V9M-3 6H3"/>
      </symbol>
      <symbol id="ico-post" viewBox="-10 -10 20 20">
        <circle class="icon-line" cx="-3" cy="-3" r="4.5"/>
        <path class="icon-line" d="M-3 1.5V8M-5.5 5H-0.5"/>
        <rect class="icon-line" x="2" y="-1" width="7" height="7" rx="1"/>
        <path class="icon-line" d="M2 1.5H9"/>
      </symbol>
      <symbol id="ico-hyst" viewBox="-10 -10 20 20">
        <circle class="icon-line" cx="0" cy="-3" r="5"/>
        <path class="icon-line" d="M0 2V9M-3 6H3M-7 7L7 -9"/>
      </symbol>
      <linearGradient id="pinkFade" x1="0" y1="0" x2="0" y2="1">
        <stop offset="0" stop-color="#efd0d4"/>
        <stop offset="0.35" stop-color="#dc7d88"/>
        <stop offset="1" stop-color="#d35a68"/>
      </linearGradient>
      <linearGradient id="photoWarm" x1="0" y1="0" x2="1" y2="1">
        <stop offset="0" stop-color="#ece3da"/>
        <stop offset="1" stop-color="#b89a88"/>
      </linearGradient>
      <linearGradient id="bundle" x1="0" y1="0" x2="0" y2="1">
        <stop offset="0" stop-color="#fbfbfb"/>
        <stop offset="0.6" stop-color="#eef1ef"/>
        <stop offset="0.85" stop-color="#c9ddd4"/>
        <stop offset="1" stop-color="#2f6f5b"/>
      </linearGradient>
    </defs>
    <rect width="532" height="532" fill="url(#pinkFade)"/>
    <path role="img" aria-label="Photo of a smiling woman with short grey hair" d="M0 0H258L248 30 262 60 244 92 256 125 240 160 258 196 244 228 262 262 252 300 0 300Z" fill="url(#photoWarm)"/>
    <circle cx="143" cy="388" r="178" fill="var(--rose-deep)"/>
    <path d="M0 430 L80 532 M0 445 L72 532 M0 460 L62 532" stroke="#f0c6cc" stroke-width="1"/>
    <g role="img" aria-label="Lunaria Harmony Set: two cream tubes and a supplement bottle">
      <rect x="40" y="250" width="212" height="264" rx="10" fill="url(#bundle)"/>
      <text class="bundle-name" x="146" y="382" font-size="13" text-anchor="middle">Lunaria Harmony Set</text>
    </g>
    <path d="M273 220 L518 214 L514 280 L276 284 Z" fill="var(--tag)"/>
    <path d="M273 310 L518 304 L514 370 L276 374 Z" fill="var(--tag)"/>
    <path d="M273 401 L518 395 L514 461 L276 465 Z" fill="var(--tag)"/>
    <circle class="badge" cx="318" cy="249" r="23"/><circle class="badge-ring" cx="318" cy="249" r="20"/>
    <circle class="badge" cx="318" cy="339" r="23"/><circle class="badge-ring" cx="318" cy="339" r="20"/>
    <circle class="badge" cx="318" cy="430" r="23"/><circle class="badge-ring" cx="318" cy="430" r="20"/>
    <use href="#ico-meno" x="305" y="236" width="26" height="26"/>
    <use href="#ico-post" x="305" y="326" width="26" height="26"/>
    <use href="#ico-hyst" x="305" y="417" width="26" height="26"/>
  </svg>
  <div class="txt" style="left:266px;top:46px;font-size:19px;font-weight:500;color:var(--rose)">AN EASIER WAY TO</div>
  <div class="txt" style="left:265px;top:74px;font-size:32px;font-weight:600;color:var(--white);line-height:39px">LOSE WEIGHT<br>DURING</div>
  <div class="txt" style="left:265px;top:157px;font-size:23px;font-weight:300;color:var(--ink)">MENOPAUSE</div>
  <div class="txt tag-label" style="left:351px;top:239px;font-size:17px">Menopause</div>
  <div class="txt tag-label" style="left:351px;top:329px;font-size:17px">Post-Menopause</div>
  <div class="txt tag-label" style="left:351px;top:420px;font-size:17px">Hysterectomy</div>
</section>

<!-- Post 2: symptoms -->
<section class="post post--struggle">
  <svg viewBox="0 0 532 532">
    <defs>
      <linearGradient id="photoStreet" x1="0" y1="0" x2="1" y2="1">
        <stop offset="0" stop-color="#8e7466"/>
        <stop offset="0.5" stop-color="#c7b4a8"/>
        <stop offset="1" stop-color="#6c5a52"/>
      </linearGradient>
    </defs>
    <rect width="532" height="532" fill="var(--rose)"/>
    <path role="img" aria-label="Photo of a smiling woman with curly grey hair" d="M0 0H532V266Q300 345 0 253Z" fill="url(#photoStreet)"/>
    <path d="M0 253Q300 345 532 266L532 272Q300 352 0 264Z" fill="var(--rose-pale)"/>
    <g role="img" aria-label="Lunaria Harmony Set: two cream tubes and a supplement bottle">
      <rect x="305" y="72" width="200" height="252" rx="10" fill="url(#bundle)"/>
      <text class="bundle-name" x="405" y="202" font-size="12" text-anchor="middle">Lunaria Harmony Set</text>
    </g>
    <line x1="33" y1="441" x2="499" y2="441" stroke="var(--white)" stroke-width="1.5"/>
    <path d="M21 460 L168 458 L165 499 L18 501 Z" fill="var(--tag)"/>
    <path d="M195 460 L342 458 L339 499 L192 501 Z" fill="var(--tag)"/>
    <path d="M368 458 L515 456 L512 497 L365 499 Z" fill="var(--tag)"/>
    <circle class="badge" cx="54" cy="480" r="14"/><circle class="badge-ring" cx="54" cy="480" r="12"/>
    <circle class="badge" cx="228" cy="480" r="14"/><circle class="badge-ring" cx="228" cy="480" r="12"/>
    <circle class="badge" cx="401" cy="478" r="14"/><circle class="badge-ring" cx="401" cy="478" r="12"/>
    <use href="#ico-meno" x="46" y="472" width="16" height="16"/>
    <use href="#ico-post" x="220" y="472" width="16" height="16"/>
    <use href="#ico-hyst" x="393" y="470" width="16" height="16"/>
  </svg>
  <div class="txt" style="left:0;width:532px;text-align:center;top:352px;font-size:21px;font-weight:800;color:var(--white);line-height:27px">STRUGGLING WITH<br>MENOPAUSE SYMPTOMS?</div>
  <div class="txt" style="left:0;width:532px;text-align:center;top:410px;font-size:16px;font-weight:300;color:var(--white)">THE SOLUTION YOU’VE BEEN WAITING FOR!</div>
  <div class="txt tag-label" style="left:73px;top:475px;font-size:10px">Menopause</div>
  <div class="txt tag-label" style="left:247px;top:475px;font-size:10px">Post-Menopause</div>
  <div class="txt tag-label" style="left:420px;top:473px;font-size:10px">Hysterectomy</div>
</section>

<!-- Post 3: relief -->
<section class="post post--relief">
  <svg viewBox="0 0 532 532">
    <defs>
      <linearGradient id="photoHome" x1="0" y1="0" x2="1" y2="1">
        <stop offset="0" stop-color="#c9bdb1"/>
        <stop offset="0.6" stop-color="#8a6a58"/>
        <stop offset="1" stop-color="#3a2c28"/>
      </linearGradient>
    </defs>
    <circle cx="-120" cy="323" r="420" fill="var(--rose-soft)"/>
    <circle role="img" aria-label="Photo of a smiling woman holding the Lunaria Harmony Set products" cx="-120" cy="323" r="400" fill="url(#photoHome)"/>
    <g role="img" aria-label="Lunaria Harmony Set product bundle">
      <rect x="323" y="323" width="146" height="186" rx="8" fill="url(#bundle)"/>
      <text class="bundle-name" x="396" y="417" font-size="10" text-anchor="middle">Lunaria Harmony Set</text>
    </g>
    <circle class="badge" cx="322" cy="145" r="24"/><circle class="badge-ring" cx="322" cy="145" r="21"/>
    <circle class="badge" cx="322" cy="211" r="24"/><circle class="badge-ring" cx="322" cy="211" r="21"/>
    <circle class="badge" cx="322" cy="279" r="24"/><circle class="badge-ring" cx="322" cy="279" r="21"/>
    <use href="#ico-meno" x="308" y="131" width="28" height="28"/>
    <use href="#ico-post" x="308" y="197" width="28" height="28"/>
    <use href="#ico-hyst" x="308" y="265" width="28" height="28"/>
  </svg>
  <div class="txt" style="right:26px;top:52px;font-size:21px;font-weight:800;color:var(--ink)">MENOPAUSE RELIEF IS HERE</div>
  <div class="txt" style="right:26px;top:81px;font-size:19px;font-weight:300;color:var(--ink)">GET YOUR LIFE BACK TODAY!</div>
  <div class="txt tag-label" style="left:357px;top:136px;font-size:18px">Menopause</div>
  <div class="txt tag-label" style="left:357px;top:202px;font-size:18px">Post-Menopause</div>
  <div class="txt tag-label" style="left:357px;top:270px;font-size:18px">Hysterectomy</div>
</section>

<!-- Post 4: weight gain -->
<section class="post post--tracks">
  <svg viewBox="0 0 532 532">
    <defs>
      <linearGradient id="photoLeft" x1="0" y1="0" x2="1" y2="1">
        <stop offset="0" stop-color="#b9b4ae"/>
        <stop offset="1" stop-color="#4e4642"/>
      </linearGradient>
      <linearGradient id="photoRight" x1="1" y1="0" x2="0" y2="1">
        <stop offset="0" stop-color="#d6d8d9"/>
        <stop offset="1" stop-color="#3b3433"/>
      </linearGradient>
    </defs>
    <line x1="84" y1="137" x2="263" y2="161" stroke="#bbbbbb" stroke-width="1" stroke-dasharray="4 3"/>
    <line x1="263" y1="161" x2="435" y2="135" stroke="#bbbbbb" stroke-width="1" stroke-dasharray="4 3"/>
    <circle class="badge" cx="84" cy="137" r="25"/><circle class="badge-ring" cx="84" cy="137" r="22"/>
    <circle class="badge" cx="263" cy="161" r="25"/><circle class="badge-ring" cx="263" cy="161" r="22"/>
    <circle class="badge" cx="435" cy="135" r="25"/><circle class="badge-ring" cx="435" cy="135" r="22"/>
    <use href="#ico-meno" x="69" y="122" width="30" height="30"/>
    <use href="#ico-post" x="248" y="146" width="30" height="30"/>
    <use href="#ico-hyst" x="420" y="120" width="30" height="30"/>
    <polygon role="img" aria-label="Photo of a smiling woman with curly grey hair" points="0,272 258,368 258,532 0,532" fill="url(#photoLeft)"/>
    <polygon role="img" aria-label="Photo of a smiling woman with silver hair in a black blazer" points="264,368 532,272 532,532 264,532" fill="url(#photoRight)"/>
    <rect x="258" y="360" width="6" height="172" fill="var(--rose)"/>
    <polygon points="0,238 0,258 200,334 205,322" fill="var(--teal)"/>
    <polygon points="0,262 0,278 200,352 204,340" fill="var(--rose)"/>
    <polygon points="532,238 532,258 332,334 327,322" fill="var(--teal)"/>
    <polygon points="532,262 532,278 332,352 328,340" fill="var(--rose)"/>
    <circle cx="263" cy="320" r="90" fill="var(--white)"/>
    <rect x="190" y="230" width="146" height="90" fill="var(--white)"/>
    <g role="img" aria-label="Lunaria Harmony Set product bundle">
      <rect x="213" y="245" width="106" height="134" rx="6" fill="url(#bundle)"/>
      <text class="bundle-name" x="266" y="315" font-size="8" text-anchor="middle">Lunaria Harmony Set</text>
    </g>
  </svg>
  <div class="txt" style="left:0;width:532px;text-align:center;top:33px;font-size:22px;font-weight:300;color:var(--ink)">STOP MENOPAUSE</div>
  <div class="txt" style="left:0;width:532px;text-align:center;top:61px;font-size:21px;font-weight:800;color:var(--ink)">WEIGHT GAIN IN ITS TRACKS!</div>
  <div class="txt tag-label" style="left:4px;width:160px;text-align:center;top:173px;font-size:18px">Menopause</div>
  <div class="txt tag-label" style="left:163px;width:200px;text-align:center;top:198px;font-size:18px">Post-Menopause</div>
  <div class="txt tag-label" style="left:345px;width:180px;text-align:center;top:167px;font-size:18px">Hysterectomy</div>
</section>

</body>
</html>
```